Promotion for a free HTML weather widget

skyvelta (http://www.skyvelta-example.com/) is a meteorological service based in Basel, Switzerland.
We offer a free HTML widget that offers weather forecasts for a selected location anywhere on the world for up to seven days (see http://www.skyvelta-example.com/en_GB/weather/forecast/widgetsetup) which can be included in any other website.
To make the widget more popular and well-known, we would like to add a promotional banner for it on our own homepage. The space where the banner will be located is marked red on the attached banner_location.png.
We have received permissions from three websites that are already using our widget to use a screenshot from their website on this banner.
These websites are:
- http://gazette.lumorix-example.ch/ (widget is on the bottom of the page)
- http://www.tonvillage-example.info/
- http://www.valbruna-example.net/
Requirements
Must have
- - Width: 696px
- Height: 150px to 200px
- fits nicely in our website
- uses screenshots of the three aforementioned websites (widget must be visible, other ads on those website must be unrecognisable)
- Text (English) that praises the most important advantages of the widget: it is free to use, worldwide available, easy to integrate, offers valuable weather information to visitors
- Possibility to change the text on our side for translations

```html
<!DOCTYPE html>
<html lang="en">
<head>
<meta charset="utf-8">
<title>skyvelta – Basel weather</title>
<link rel="stylesheet" href="https://fonts.googleapis.com/css2?family=Arimo:wght@400;700&family=Nunito:wght@800&display=swap">
<style>
  :root {
    --page-bg: #ececec;
    --panel-bg: #ffffff;
    --panel-border: #c4c4c4;
    --text: #333333;
    --heading: #2b2b2b;
    --accent-blue: #1b7fd6;
    --muted: #9a9a9a;
    --map-tone: #dcdfe2;
    --map-edge: #b9bec4;
    --banner-top: #5ca8df;
    --banner-mid: #8cc4ec;
    --banner-bottom: #eaf4fb;
    --url-bar: #1d8ee2;
    --shot-fill: #f3f3f3;
    --temp-line: #f2600c;
    --temp-fill: #fbd2a8;
    --day-band: #f7f28c;
    --axis-red: #e8571a;
    --min-blue: #2564c0;
  }
  * { margin: 0; padding: 0; box-sizing: border-box; }
  html, body { width: 1200px; height: 766px; overflow: hidden; }
  body {
    background: var(--page-bg);
    font-family: "Arimo", Arial, sans-serif;
    color: var(--text);
    position: relative;
  }
  .panel {
    position: absolute;
    left: 185px;
    width: 830px;
    background: var(--panel-bg);
    border: 1px solid var(--panel-border);
  }
  .radar-panel { top: -2px; height: 262px; }
  .radar-map {
    position: absolute; left: 12px; top: 27px; width: 222px; height: 217px;
    background: linear-gradient(135deg, #e6e8ea, var(--map-tone) 60%, #cfd4d8);
    border: 1px solid var(--map-edge);
  }
  .forecast-title {
    position: absolute; left: 276px; top: 26px; font-size: 19px; font-weight: 400; color: var(--heading);
  }
  .radar-anim {
    position: absolute; left: 276px; top: 67px; width: 146px; height: 152px;
    background: linear-gradient(160deg, #e9e9e9, #cdcdcd);
    border: 1px solid #8a8a8a;
  }
  .forecast-text {
    position: absolute; left: 445px; top: 67px; width: 352px;
    font-size: 16.5px; line-height: 25.5px;
  }
  .forecast-text .amount { color: var(--accent-blue); font-weight: 700; }
  .forecast-text p + p { margin-top: 6px; }
  .help-link {
    position: absolute; left: 445px; top: 217px; font-size: 16.5px; color: var(--muted);
    display: flex; align-items: center; gap: 8px;
  }
  .help-link .icon {
    width: 20px; height: 20px; background: #a5a5a5; color: #fff;
    font-weight: 700; font-size: 14px; text-align: center; line-height: 20px;
  }

  .widget-banner {
    position: absolute; left: 185px; top: 273px; width: 830px; height: 240px;
    background: linear-gradient(var(--banner-top), var(--banner-mid) 62%, var(--banner-bottom));
    border: 1px solid #b7cfe2;
    overflow: hidden;
  }
  .benefits {
    font-family: "Nunito", "Arial Rounded MT Bold", sans-serif;
    font-weight: 800; color: #fff; font-size: 26px;
    text-shadow: 0 1px 2px rgba(20,60,100,.55);
    position: absolute; left: 0; width: 100%;
  }
  .benefits.row-one { top: 7px; }
  .benefits.row-one span { position: absolute; white-space: nowrap; }
  .benefits.row-two { top: 36px; text-align: center; padding-right: 28px; white-space: nowrap; }
  .site-shot {
    position: absolute; top: 75px; height: 123px;
    background: linear-gradient(var(--shot-fill), #e3e3e3);
    box-shadow: 0 0 3px rgba(0,0,0,.25);
  }
  .site-shot .url {
    height: 17px; background: var(--url-bar); color: #fff;
    font-size: 11px; line-height: 17px; text-align: center;
    white-space: nowrap; letter-spacing: -0.1px;
  }
  .site-shot .body { height: 106px; }
  .shot-one { left: 87px; width: 208px; }
  .shot-one .body { background: linear-gradient(90deg, #fafafa 35%, #eaf3d6 35%, #f5f5f5 70%); }
  .shot-two { left: 302px; width: 222px; }
  .shot-two .body { background: linear-gradient(90deg, #c89a4e 0 18%, #f6f6f6 18% 80%, #d9e7c7 80%); }
  .shot-three { left: 533px; width: 208px; }
  .shot-three .body { background: linear-gradient(90deg, #6b5a3e 0 12%, #eef0ea 12% 60%, #f8f8f8 60%); }
  .reflection {
    position: absolute; top: 199px; height: 30px;
    background: linear-gradient(rgba(255,255,255,.55), rgba(255,255,255,0));
  }

  .meteogram-panel { top: 528px; height: 250px; }
  .meteogram-title {
    position: absolute; left: 12px; top: 8px; font-size: 23px; font-weight: 700; color: var(--heading);
  }
  .meteogram-head-rule {
    position: absolute; left: 0; right: 0; top: 37px; border-top: 1px solid #e2e2e2;
  }
  .meteogram-chart { position: absolute; left: -1px; top: 61px; width: 830px; height: 176px; }
</style>
</head>
<body>

<section class="panel radar-panel">
  <div class="radar-map" role="img" aria-label="Precipitation radar map of Switzerland with city markers"></div>
  <h2 class="forecast-title">Local short-term precipitation forecast</h2>
  <div class="radar-anim" role="img" aria-label="Animated local precipitation radar centred on Basel, 05.08 12:25"></div>
  <div class="forecast-text">
    <p><span class="amount">0 mm</span> Precipitation in Basel at 11:30-12:40</p>
    <p>The animation shows the distribution of precipitation for the next hour. Lightning of the past half hour is displayed as red crosses. Basel is located in the center.</p>
  </div>
  <div class="help-link"><span class="icon">?</span>Show help</div>
</section>

<section class="widget-banner">
  <div class="benefits row-one">
    <span style="left:64px">Free to use</span>
    <span style="left:246px">Worldwide available</span>
    <span style="left:545px">Easy to integrate</span>
  </div>
  <div class="benefits row-two">Offers valuable weather information to visitors</div>

  <div class="site-shot shot-one">
    <div class="url">http://gazette.lumorix-example.ch/</div>
    <div class="body" role="img" aria-label="Screenshot of the gazette website with the weather widget"></div>
  </div>
  <div class="site-shot shot-two">
    <div class="url">http://www.tonvillage-example.info/</div>
    <div class="body" role="img" aria-label="Screenshot of the village website with the weather widget"></div>
  </div>
  <div class="site-shot shot-three">
    <div class="url">http://www.valbruna-example.net/</div>
    <div class="body" role="img" aria-label="Screenshot of the valley website with the weather widget"></div>
  </div>
  <div class="reflection" style="left:87px;width:208px"></div>
  <div class="reflection" style="left:302px;width:222px"></div>
  <div class="reflection" style="left:533px;width:208px"></div>
</section>

<section class="panel meteogram-panel">
  <h2 class="meteogram-title">Meteogram - 5 days - Basel</h2>
  <div class="meteogram-head-rule"></div>
  <svg class="meteogram-chart" viewBox="155 495 696 147.5" font-family="Arimo, Arial, sans-serif">
    <text x="157" y="515" font-size="10" font-weight="700" fill="#1b5fc0">47.57°N / 7.60°E (263m asl)</text>
    <text x="845" y="506" font-size="15" fill="#666" text-anchor="end">skyvelta</text>
    <text x="845" y="516" font-size="7" fill="#666" text-anchor="end">www.skyvelta-example.com</text>

    <g font-size="11" font-weight="700" fill="#222" text-anchor="middle">
      <text x="263" y="526" font-weight="400">05.08</text><text x="263" y="539" font-size="12.5">Monday</text>
      <text x="381" y="526" font-weight="400">06.08</text><text x="381" y="539" font-size="12.5">Tuesday</text>
      <text x="500" y="526" font-weight="400">07.08</text><text x="500" y="539" font-size="12.5">Wednesday</text>
      <text x="618" y="526" font-weight="400">08.08</text><text x="618" y="539" font-size="12.5">Thursday</text>
      <text x="736" y="526" font-weight="400">09.08</text><text x="736" y="539" font-size="12.5">Friday</text>
    </g>

    <g fill="var(--day-band)">
      <rect x="234" y="545" width="89" height="90"/>
      <rect x="352" y="545" width="74" height="90"/>
      <rect x="470" y="545" width="88" height="90"/>
      <rect x="590" y="545" width="72" height="90"/>
      <rect x="707" y="545" width="73" height="90"/>
    </g>
    <g stroke="#b8b8b8" stroke-width="0.6" stroke-dasharray="1.5 1.5">
      <path d="M204 545V635M233 545V635M263 545V635M292 545V635M322 545V635M351 545V635M381 545V635M410 545V635M440 545V635M469 545V635M499 545V635M528 545V635M558 545V635M587 545V635M617 545V635M646 545V635M676 545V635M705 545V635M735 545V635M764 545V635M796 545V635"/>
    </g>
    <rect x="204" y="618" width="592" height="8" fill="#c7ec9a"/>
    <rect x="204" y="626" width="592" height="10" fill="#35c23a"/>

    <path d="M204 615 C240 612 260 577 290 577 C318 577 330 609 350 609 C368 609 375 580 395 580 C425 580 440 615 470 615 C495 615 500 590 520 590 C545 590 560 618 585 618 C610 618 620 602 640 602 C665 602 670 621 690 621 C720 621 735 602 755 602 C775 602 785 614 796 615 L796 618 L204 618 Z" fill="var(--temp-fill)"/>
    <path d="M204 615 C240 612 260 577 290 577 C318 577 330 609 350 609 C368 609 375 580 395 580 C425 580 440 615 470 615 C495 615 500 590 520 590 C545 590 560 618 585 618 C610 618 620 602 640 602 C665 602 670 621 690 621 C720 621 735 602 755 602 C775 602 785 614 796 615" fill="none" stroke="var(--temp-line)" stroke-width="2.2"/>

    <g font-size="12" font-weight="700" text-anchor="middle" fill="#111">
      <text x="292" y="589">32</text><text x="406" y="594">31</text>
      <text x="520" y="603">28</text><text x="642" y="615">24</text><text x="760" y="615">24</text>
    </g>
    <g font-size="12" font-weight="700" text-anchor="middle" fill="var(--min-blue)">
      <text x="363" y="622">22</text><text x="481" y="626">20</text><text x="585" y="630">19</text>
    </g>

    <g font-size="11" font-weight="700" fill="var(--axis-red)" text-anchor="end">
      <text x="199" y="556">40</text><text x="199" y="571">35</text><text x="199" y="587">30</text>
      <text x="199" y="603">25</text><text x="199" y="619">20</text><text x="199" y="635">15</text>
    </g>
    <g font-size="11" font-weight="700" fill="var(--axis-red)">
      <text x="801" y="556">40</text><text x="801" y="571">35</text><text x="801" y="587">30</text>
      <text x="801" y="603">25</text><text x="801" y="619">20</text><text x="801" y="635">15</text>
    </g>
    <text transform="translate(171 622) rotate(-90)" font-size="11" font-weight="700" fill="var(--axis-red)">Temp. (°C)</text>

    <g fill="#f5c400" stroke="#e09b00" stroke-width="0.8">
      <circle cx="262" cy="567" r="5.5"/><circle cx="300" cy="553" r="5.5"/>
    </g>
    <g fill="#f5c400" stroke="#e09b00" stroke-width="0.8">
      <circle cx="491" cy="572" r="4.5"/><circle cx="537" cy="568" r="4.5"/>
      <circle cx="616" cy="582" r="4.5"/><circle cx="653" cy="576" r="4.5"/>
      <circle cx="731" cy="580" r="4.5"/><circle cx="766" cy="582" r="4.5"/>
      <circle cx="380" cy="564" r="4"/><circle cx="421" cy="566" r="4"/>
    </g>
    <g fill="#cfe1f0" stroke="#5b7fa3" stroke-width="0.8">
      <ellipse cx="387" cy="570" rx="8" ry="5"/><ellipse cx="427" cy="572" rx="8" ry="5"/>
      <ellipse cx="499" cy="578" rx="8" ry="5"/><ellipse cx="545" cy="574" rx="8" ry="5"/>
      <ellipse cx="580" cy="589" rx="9" ry="5.5"/><ellipse cx="624" cy="588" rx="8" ry="5"/>
      <ellipse cx="661" cy="582" rx="8" ry="5"/><ellipse cx="739" cy="586" rx="8" ry="5"/>
      <ellipse cx="774" cy="588" rx="8" ry="5"/>
    </g>
    <g stroke="#2d68b8" stroke-width="1">
      <path d="M383 577l-1 4M388 577l-1 4M392 577l-1 4M423 579l-1 4M428 579l-1 4M541 581l-1 4M546 581l-1 4M576 596l-1 4M581 596l-1 4M586 596l-1 4"/>
    </g>
    <g fill="#4a4a4a">
      <path d="M348 564a7 7 0 1 0 3 11a6 6 0 1 1 -3 -11z"/>
      <path d="M461 574a7 7 0 1 0 3 11a6 6 0 1 1 -3 -11z"/>
      <path d="M696 594a7 7 0 1 0 3 11a6 6 0 1 1 -3 -11z"/>
    </g>
  </svg>
</section>

</body>
</html>
```